Luxury Lifestyle service requires name card

Logo of my company has to be on the left side of the card. (Blue logo)Name and information preferably on the right side.QR code inclusion would be great , Gold logo if it can be included at the back of the card would be great too- we are a luxury lifestyle concierge company catering to the high net worth clients.

Target Market(s)

high net worth customers / luxury

Industry/Entity Type

Business Service

Contact Information for Business Card

name
contact
email
website

Font styles to use
Serif

Colors
0255a3
3176b5
85abd2
0492cd
33a6d7
85cae6
cee9f5

Requirements
Must have
• Logo of my company has to be on the left side of the card. (Blue logo)
• Name and information on the right side.
Nice to have
• QR code inclusion would be great
Should not have
• Do not use colours :- red , purple , orange , yellow
• background card colour : do not use black

```html
<!DOCTYPE html>
<html lang="en">
<head>
<meta charset="utf-8">
<title>Lumen Crest – Business Card</title>
<link href="https://fonts.googleapis.com/css2?family=Cinzel:wght@400;600&family=Lora:wght@400;700&display=swap" rel="stylesheet">
<style>
  :root {
    --backdrop: #9e9e9e;
    --card-white: #ffffff;
    --ink: #2b2b2b;
    --accent: #0492cd;
    --accent-deep: #0255a3;
    --sky-top: #03ade6;
    --sky-mid: #00d9f6;
    --sky-bottom: #03ade6;
    --on-sky: #ffffff;
    --gold: #8a6a1c;
  }
  * { box-sizing: border-box; margin: 0; padding: 0; }
  html, body {
    width: 1200px; height: 900px; overflow: hidden;
    background: var(--backdrop);
  }
  .canvas { position: relative; width: 1200px; height: 900px; }

  .card {
    position: absolute; top: 200px; width: 310px; height: 502px;
  }
  .card--front {
    left: 253px; background: var(--card-white);
    border-radius: 62px 0 62px 0;
  }
  .card--back {
    left: 627px;
    background: linear-gradient(180deg, var(--sky-top) 0%, var(--sky-mid) 50%, var(--sky-bottom) 100%);
    border-radius: 0 62px 0 62px;
  }

  /* Front: brand block on the left */
  .brand {
    position: absolute; left: 33px; top: 74px;
  }
  .brand__circle {
    width: 96px; height: 96px; border-radius: 50%;
    border: 3px solid var(--accent);
  }
  .brand__name {
    margin-top: 20px;
    font-family: "Cinzel", serif; font-weight: 400; font-size: 25px;
    letter-spacing: 1px; color: var(--accent-deep); white-space: nowrap;
  }

  /* Front: details on the right */
  .contact {
    position: absolute; right: 30px; top: 318px; text-align: right;
    font-family: "Lora", serif; color: var(--ink);
  }
  .contact__name { font-weight: 700; font-size: 21px; color: var(--accent); letter-spacing: 0.5px; }
  .contact__role { font-size: 13.5px; margin-top: 1px; }
  .contact__list { list-style: none; margin-top: 10px; }
  .contact__list li {
    display: flex; align-items: center; justify-content: flex-end;
    font-size: 14px; height: 19px; white-space: nowrap;
  }
  .contact__list svg { width: 12px; height: 12px; margin-right: 6px; fill: var(--accent); }
  .contact__address { font-size: 14px; line-height: 19px; margin-top: 6px; }

  /* Back: gold name with a plain circle */
  .back-brand {
    position: absolute; left: 0; right: 0; top: 150px;
    display: flex; flex-direction: column; align-items: center;
  }
  .back-brand__circle {
    width: 130px; height: 130px; border-radius: 50%;
    border: 3px solid var(--on-sky);
  }
  .back-brand__name {
    margin-top: 24px;
    font-family: "Cinzel", serif; font-weight: 600; font-size: 25px;
    letter-spacing: 1px; color: var(--gold); white-space: nowrap;
  }
</style>
</head>
<body>
<main class="canvas">
  <section class="card card--front">
    <div class="brand">
      <div class="brand__circle" aria-hidden="true"></div>
      <p class="brand__name">LUMEN CREST</p>
    </div>

    <div class="contact">
      <p class="contact__name">ADRIAN VALE</p>
      <p class="contact__role">Managing Director</p>
      <ul class="contact__list">
        <li><svg viewBox="0 0 12 12" aria-hidden="true"><path d="M2 1h2.5l1 2.5-1.3 1a6 6 0 0 0 3.3 3.3l1-1.3L11 7.5V10a1 1 0 0 1-1 1A9 9 0 0 1 1 2a1 1 0 0 1 1-1z"/></svg>055-987 654 321</li>
        <li><svg viewBox="0 0 12 12" aria-hidden="true"><path d="M1 2.5h10v7H1z M1.5 3l4.5 3.5L10.5 3" stroke="#fff" stroke-width="0.8"/></svg>info@lumencrest.com</li>
        <li><svg viewBox="0 0 12 12" aria-hidden="true"><circle cx="6" cy="6" r="5"/><path d="M1 6h10M6 1c2 2 2 8 0 10M6 1c-2 2-2 8 0 10" stroke="#fff" stroke-width="0.7" fill="none"/></svg>www.lumencrest.com</li>
      </ul>
      <p class="contact__address">12345, Address Goes Here<br>Country Name, 123456</p>
    </div>
  </section>

  <section class="card card--back">
    <div class="back-brand">
      <div class="back-brand__circle" aria-hidden="true"></div>
      <p class="back-brand__name">LUMEN CREST</p>
    </div>
  </section>
</main>
</body>
</html>
```